Visitenkarten-Design für Erfindung & Entwicklung von Produkten für Körper, Geist und Seele
Zielgruppe
Erfindung und Entwicklung von Produkten für Körper Geist und Seele
Als grosser Überbegriff Produkte zur Regenration und Wohlbefinden sowie Bewusstseins Förderung
' Beispiel ' www. o-senva.ch
Zielgruppe Jedermann und Jedefrau die Ihr Bewusstein für Ihre Gesundheit und Heilung auf allen Ebenen vertiefen möchte ....
Aufgabenstellung
Das Logo ist Entwickelt in einem Entwurfsstadium kleine Verbesserungsvorschläge wären möglich
Vorallem geht es um das Layout und der sauberen Daten Erfassung
sowie die Gestaltung der Visitenkarte

```html
<!DOCTYPE html>
<html lang="de">
<head>
<meta charset="utf-8">
<title>Visitenkarte velunor</title>
<link rel="stylesheet" href="https://fonts.googleapis.com/css2?family=Open+Sans:wght@400;600&display=swap">
<style>
  :root {
    --backdrop: #2b2d30;
    --card: #ffffff;
    --leaf-green: #4f8a2c;
    --name-green: #3f7d22;
    --gold: #a88a2a;
    --ink: #2f2f2f;
    --rule: #9a9a9a;
    --pattern-sage: #b9c8b2;
    --pattern-cream: #e6dcb8;
    --pattern-grey: #a9aca8;
  }
  html, body {
    margin: 0;
    width: 1200px;
    height: 898px;
    overflow: hidden;
    background: var(--backdrop);
    font-family: "Open Sans", sans-serif;
  }
  .sheet {
    position: relative;
    width: 1200px;
    height: 898px;
  }
  .card {
    position: absolute;
    left: 320px;
    width: 560px;
    height: 362px;
    border-radius: 22px;
    overflow: hidden;
    box-shadow: 0 8px 24px rgba(0,0,0,.35);
  }
  .card--front { top: 66px; background: var(--card); }
  .card--back { top: 470px; }

  /* front */
  .brand {
    position: absolute;
    left: 46px;
    top: 50px;
    display: flex;
    align-items: center;
    gap: 12px;
  }
  .brand__mark {
    width: 26px;
    height: 26px;
    background: var(--leaf-green);
  }
  .brand__name {
    font-family: "Open Sans", sans-serif;
    font-weight: 600;
    font-size: 30px;
    color: var(--ink);
  }
  .motto {
    position: absolute;
    left: 84px;
    top: 100px;
    font-size: 15px;
    font-weight: 400;
    color: var(--gold);
  }
  .divider {
    position: absolute;
    left: 190px;
    top: 168px;
    width: 1px;
    height: 150px;
    background: var(--rule);
  }
  .icons {
    position: absolute;
    left: 164px;
    top: 214px;
    display: flex;
    flex-direction: column;
    gap: 6px;
  }
  .icons svg { width: 14px; height: 14px; fill: var(--leaf-green); }
  .contact {
    position: absolute;
    left: 206px;
    top: 164px;
    color: var(--ink);
  }
  .contact__name {
    margin: 0;
    font-size: 21px;
    font-weight: 600;
    color: var(--name-green);
    letter-spacing: .5px;
  }
  .contact__role {
    margin: 0 0 8px;
    font-size: 14px;
  }
  .contact__lines {
    margin: 0;
    padding: 0;
    list-style: none;
    font-size: 14px;
    line-height: 20px;
  }

  /* back */
  .pattern {
    position: absolute;
    inset: 0;
    background:
      radial-gradient(circle at 30% 40%, var(--pattern-cream) 0, transparent 45%),
      radial-gradient(circle at 75% 70%, var(--pattern-sage) 0, transparent 50%),
      linear-gradient(135deg, var(--pattern-sage), var(--pattern-grey) 55%, var(--pattern-sage));
  }
  .back-brand {
    position: absolute;
    left: 0;
    right: 0;
    top: 140px;
    display: flex;
    justify-content: center;
    align-items: center;
    gap: 14px;
  }
  .back-brand .brand__mark { width: 32px; height: 32px; }
  .back-brand .brand__name { font-size: 38px; }
  .card--back .motto {
    left: 0;
    right: 0;
    top: 200px;
    text-align: center;
    font-size: 17px;
  }
</style>
</head>
<body>
<main class="sheet">
  <section class="card card--front" aria-label="Vorderseite">
    <div class="brand">
      <span class="brand__mark"></span>
      <span class="brand__name">velunor</span>
    </div>
    <span class="motto">klar gedacht</span>
    <div class="divider"></div>
    <div class="icons" aria-hidden="true">
      <svg viewBox="0 0 16 16"><path d="M4 1l3 3-2 2c1 2 3 4 5 5l2-2 3 3-2 3C7 15 1 9 1 3z"/></svg>
      <svg viewBox="0 0 16 16"><path d="M1 3h14v10H1zM2 4l6 5 6-5v1L8 10 2 5z" fill-rule="evenodd"/></svg>
      <svg viewBox="0 0 16 16"><circle cx="8" cy="8" r="6.5" fill="none" stroke="#4f8a2c" stroke-width="1.5"/><path d="M1.5 8h13M8 1.5c-3 3-3 10 0 13M8 1.5c3 3 3 10 0 13" fill="none" stroke="#4f8a2c" stroke-width="1.2"/></svg>
      <svg viewBox="0 0 16 16"><path d="M8 1a5 5 0 0 1 5 5c0 4-5 9-5 9S3 10 3 6a5 5 0 0 1 5-5zm0 3a2 2 0 1 0 0 4 2 2 0 0 0 0-4z" fill-rule="evenodd"/></svg>
    </div>
    <div class="contact">
      <h1 class="contact__name">KOLU TRISVEND</h1>
      <p class="contact__role">Geschäftsführer</p>
      <ul class="contact__lines">
        <li>079 555 01 99</li>
        <li>kolutrisvend@velunor.ch</li>
        <li>www. velunor.ch</li>
        <li>Lindenweg 14 8000 MUSTERDORF</li>
      </ul>
    </div>
  </section>

  <section class="card card--back" aria-label="Rückseite">
    <div class="pattern" role="img" aria-label="Flächiges Blättermuster in Salbeigrün, Creme und Grau"></div>
    <div class="back-brand">
      <span class="brand__mark"></span>
      <span class="brand__name">velunor</span>
    </div>
    <span class="motto">klar gedacht</span>
  </section>
</main>
</body>
</html>
```